ご提案有難うございました。
最もサイトのトンマナにあっており、かつキャンペーンの売りが目立っていると感じたため、こちらのデザインを採用させて頂きました。
どれも素晴らしいご提案で御座いました。
また機会があればどうぞ宜しくお願い致します。
居酒屋予約 バナーデザイン バナー作成の仕事の依頼
希望する色 特になし・その他
バナーサイズ
• 300x250
目的・概要
居酒屋の割引キャンペーンページに誘導するために使用するバナー制作です。
依頼詳細
以下のページ等に設置致します。
https://www.pelmora-go.com/asia/japan/japa-japan/japa-restaurant/shinjuku-izakaya/
▽入れてほしい画像▽
会社ロゴ
▽入れてほしい文言▽
※以下の文章例を参考に、バナーデザインに映えるようご調整ください
■文章例
【最大100%割引】税込み2,160円以上の飲食で2,000円のキャッシュバックキャンペーン中!
【最大100%割引】居酒屋利用で2,000円のキャッシュバックキャンペーン中!
【最大100%割引】2,160円(税込)以上の居酒屋利用で2,000円の現金還元中!
Pelmora限定!居酒屋の利用で現金2,000円が貰える!
【最大100%割引】税込み2,160円の居酒屋利用で2,000円現金還元中!
Pelmora限定企画!税込み2,160円の居酒屋利用で2,000円現金還元中!!
3000店舗以上から選べる!税込み2,160円の居酒屋利用で2,000円現金還元中!!
居酒屋代金、実質最大100%オフ
3000店以上の居酒屋が実質最大100%割引
居酒屋の利用で漏れなく現金2,000円が貰える
▽バナーサイズ▽
▽納品形式▽
png/jpg
▽注意点・禁止事項▽
※他のクライアントへ既に提案した内容の転用など
※作成いただいたバナーに関して、納品後はクライアントに帰属します。
たくさんのウェブデザイナーの方からのご提案をお待ちしております!

```html
<!DOCTYPE html>
<html lang="ja">
<head>
<meta charset="utf-8">
<title>居酒屋代 実質100%OFF | Pelmora</title>
<link rel="stylesheet" href="https://fonts.googleapis.com/css2?family=M+PLUS+1p:wght@800;900&display=swap">
<style>
  :root {
    --sky: #2d9fe6;
    --sky-light: #7cc3ef;
    --sky-pale: #a9d7f4;
    --offer-red: #e8101a;
    --outline-white: #ffffff;
    --brand-blue: #1c8fe0;
    --footer-bg: #ffffff;
  }
  * { margin: 0; padding: 0; box-sizing: border-box; }
  html, body {
    width: 1200px;
    height: 1000px;
    overflow: hidden;
    background: var(--footer-bg);
  }
  .banner {
    position: relative;
    width: 1200px;
    height: 1000px;
    font-family: "M PLUS 1p", sans-serif;
  }
  .hero {
    position: absolute;
    inset: 0 0 232px 0;
    background: var(--sky);
    overflow: hidden;
  }
  .hero-art {
    position: absolute;
    inset: 0;
    background:
      radial-gradient(ellipse 320px 260px at 560px 120px, var(--sky-light) 0%, transparent 70%),
      linear-gradient(to top, var(--sky-pale) 0%, var(--sky-light) 22%, transparent 45%);
    opacity: 0.85;
  }
  .headline {
    position: absolute;
    left: 0;
    right: 0;
    text-align: center;
    color: var(--offer-red);
    font-weight: 900;
    line-height: 1;
    -webkit-text-stroke: 16px var(--outline-white);
    paint-order: stroke fill;
    white-space: nowrap;
  }
  .headline--venue { top: 64px; font-size: 142px; letter-spacing: 4px; }
  .headline--rate  { top: 300px; font-size: 186px; letter-spacing: -2px; }
  .headline--off   { top: 548px; font-size: 136px; letter-spacing: 2px; }
  .footer {
    position: absolute;
    left: 0;
    right: 0;
    bottom: 0;
    height: 232px;
    background: var(--footer-bg);
    display: flex;
    align-items: center;
    justify-content: center;
    gap: 40px;
  }
  .brand-dot {
    width: 110px;
    height: 110px;
    border-radius: 50%;
    background: var(--brand-blue);
  }
  .brand-name {
    color: var(--brand-blue);
    font-size: 118px;
    font-weight: 900;
    line-height: 1;
  }
</style>
</head>
<body>
  <main class="banner">
    <section class="hero">
      <div class="hero-art" role="img" aria-label="歓声を上げて手を挙げる人々のシルエット"></div>
      <p class="headline headline--venue">居酒屋代</p>
      <p class="headline headline--rate">実質 100%</p>
      <p class="headline headline--off">OFF</p>
    </section>
    <footer class="footer">
      <span class="brand-dot"></span>
      <span class="brand-name">Pelmora</span>
    </footer>
  </main>
</body>
</html>
```